Electrical Product Brochure Design

We have 15 electricians on the road and want to create a product brochure for them to show residential clients. I have attached all the product images in high res to be used and some images of our company and logo. I have also attached a previous product brochure that was designed which we don't want to use/has been edited. Additionally there is a Word document with the content that is needed.

Please create the brochure as a double sided A4 brochure.
Updates

Hi, Thank you for your designs. Please see the updated brief including ensuring the design is a double sided A4 flyer. Please ensure all products from the product brochure content are used on the design and all content. Please ensure Travik's contact information is used as well. Please ensure you see the updated brief for new product images I have now been able to upload as well as a few options for images of our tradespeople that can be used. Thank you.

Target Market(s)

Homeowners

Industry/Entity Type

Electrical

Font styles to use
Sans Serif

Colors
0255a3
fbed22
ec1f27

Requirements
Must have
• Travik colours including mainly blue, but also red and a bit of yellow.
• Travik's contact information including website, phone, email, and PO Box address.
• Each product's image with the content listed next to the image.
Nice to have
• If the four types of fan images could be used, and listed as one product.
• If you could also use images of our tradespeople attached as well?

```html
<!DOCTYPE html>
<html lang="en">
<head>
<meta charset="utf-8">
<title>Travik Electrical Services – Product Flyer</title>
<link rel="stylesheet" href="https://fonts.googleapis.com/css2?family=Tinos:wght@400;700&family=Open+Sans:wght@400;600;700&display=swap">
<style>
  :root {
    --brand-blue: #0255a3;
    --brand-red: #ec1f27;
    --brand-yellow: #fbed22;
    --ink: #333;
    --paper: #ffffff;
    --photo-light: #e6e8ea;
    --photo-dark: #9aa0a6;
  }
  html, body { margin: 0; padding: 0; overflow: hidden; }
  body { width: 851px; height: 1200px; background: var(--paper); }
  .flyer {
    position: relative; width: 851px; height: 1200px; overflow: hidden;
    background: var(--paper); font-family: "Open Sans", Arial, sans-serif; color: var(--ink);
  }
  .section-tab {
    position: absolute; margin: 0; background: var(--brand-blue); color: #fff;
    font-family: "Tinos", "Times New Roman", serif; font-weight: 700;
    font-size: 18px; line-height: 1.2; padding: 6px 14px;
    border-radius: 0 10px 0 10px; text-transform: uppercase; box-sizing: border-box;
  }
  .section-tab.single { white-space: nowrap; }
  .product-photo { position: absolute; border-radius: 6px; }
  .photo-white { background: radial-gradient(circle at 40% 35%, #fafafa, var(--photo-light) 60%, #c9ccd0); }
  .photo-black { background: radial-gradient(circle at 40% 35%, #6a6d72, #2a2c30 70%); }
  .photo-bronze { background: linear-gradient(180deg, #d9a877, #b07a45 55%, #8a5a2e); }
  .photo-silver { background: linear-gradient(180deg, #e2e4e6, var(--photo-dark)); }
  .copy { position: absolute; font-size: 12px; line-height: 1.4; font-weight: 600; }
  .copy h3 {
    margin: 0 0 2px; font-family: "Tinos", "Times New Roman", serif;
    font-weight: 700; font-size: 20px; line-height: 1.15; color: var(--brand-blue);
  }
  .copy p { margin: 0 0 10px; }
  .copy ul { list-style: none; margin: 0; padding: 0; }
  .footer {
    position: absolute; left: 0; top: 1118px; width: 851px; height: 82px;
    background: var(--brand-blue);
  }
  .footer-info { position: absolute; left: 22px; top: 5px; color: #fff; font-size: 12px; line-height: 1.38; }
  .footer-info .company { font-family: "Tinos", "Times New Roman", serif; font-weight: 700; font-size: 18px; line-height: 1.25; }
  .footer-info .label { color: var(--brand-red); font-weight: 700; }
  .footer-info .gap { display: inline-block; width: 34px; }
  .brand-box {
    position: absolute; right: 24px; top: 14px; width: 178px; height: 54px;
    background: #fff; border-radius: 4px; display: flex; align-items: center; justify-content: center; gap: 8px;
  }
  .brand-box .dot { width: 12px; height: 12px; background: var(--brand-yellow); border-radius: 50%; }
  .brand-box .name { font-family: "Open Sans", Arial, sans-serif; font-weight: 700; font-size: 22px; color: var(--brand-blue); letter-spacing: 1px; }
</style>
</head>
<body>
<main class="flyer">

  <!-- Safety switches -->
  <h2 class="section-tab single" style="left:40px; top:22px;">Safety Switches</h2>
  <div class="product-photo photo-white" style="left:44px; top:66px; width:118px; height:168px;" role="img" aria-label="White safety switch with red test toggle"></div>
  <div class="copy" style="left:222px; top:80px; width:580px;">
    <h3>Features</h3>
    <p>In the event of a fault this device protects you and your appliances</p>
    <h3>Benefits</h3>
    <ul>
      <li>Safety switches are sensitive to minor faults which will prevent larger fault</li>
      <li>Industry recommended devices</li>
    </ul>
  </div>

  <!-- Twin spot flood lights -->
  <h2 class="section-tab" style="left:28px; top:262px; width:470px;">Security LED Twin Spot Flood Lights (With and Without Sensor)</h2>
  <div class="product-photo photo-black" style="left:62px; top:338px; width:104px; height:112px; border-radius:50%;" role="img" aria-label="Black twin spot flood light with sensor"></div>
  <div class="product-photo photo-black" style="left:232px; top:338px; width:104px; height:112px; border-radius:50%;" role="img" aria-label="Black twin spot flood light without sensor"></div>
  <div class="copy" style="left:40px; top:478px; width:440px;">
    <h3>Features</h3>
    <p>Low heat</p>
    <h3>Benefits</h3>
    <ul>
      <li>Long lasting - low to no globe maintenance cost</li>
      <li>Energy saving</li>
      <li>Available in black or white</li>
      <li>With Sensor: Detects motion and instantly turns on LED light</li>
      <li>Timing, lux and distance adjustments</li>
    </ul>
  </div>

  <!-- Up/down light -->
  <h2 class="section-tab single" style="left:525px; top:290px; width:298px;">Up/Down Light</h2>
  <div class="product-photo photo-bronze" style="left:624px; top:336px; width:60px; height:176px; border-radius:28px;" role="img" aria-label="Bronze up/down wall pillar light"></div>
  <div class="copy" style="left:530px; top:528px; width:300px;">
    <h3>Features</h3>
    <p>Up/Down wall pillar light</p>
    <h3>Benefits</h3>
    <ul>
      <li>Available in stainless steel, solid copper, matt black, matt white, matt silver, gold, silver, titanium, and bronze</li>
      <li>Attractive option for outdoor spaces</li>
      <li>High output reflector to maximise light</li>
      <li>LED optional</li>
    </ul>
  </div>

  <!-- Double adjustable spotlights -->
  <h2 class="section-tab single" style="left:28px; top:750px; width:383px;">Double Adjustable Spotlights</h2>
  <div class="product-photo photo-silver" style="left:118px; top:796px; width:84px; height:92px;" role="img" aria-label="Silver double adjustable wall spotlight"></div>
  <div class="copy" style="left:40px; top:900px; width:380px;">
    <h3>Features</h3>
    <p>Double adjustable wall pillar lights</p>
    <h3>Benefits</h3>
    <ul>
      <li>Available in stainless steel, solid copper, matt black, matt white, matt silver, gold, silver, titanium, and bronze</li>
      <li>High output reflector to maximise light</li>
      <li>Create light in the direction you desire</li>
      <li>Attractive option for outdoor spaces</li>
    </ul>
  </div>

  <!-- LED garden spike lights -->
  <h2 class="section-tab single" style="left:440px; top:750px; width:383px;">LED Garden Spike Lights</h2>
  <div class="product-photo photo-black" style="left:445px; top:808px; width:112px; height:136px; border-radius:8px;" role="img" aria-label="Black LED garden spike lights"></div>
  <div class="copy" style="left:572px; top:822px; width:260px;">
    <h3>Features</h3>
    <p>Single or double adjustable spike spot lights</p>
    <h3>Benefits</h3>
    <ul>
      <li>Available in stainless steel, copper, matt black, gold, silver, titanium and bronze</li>
      <li>LED optional</li>
      <li>Can be used with a halogen globe</li>
      <li>Great to light up garden spaces</li>
    </ul>
  </div>

  <!-- Footer -->
  <footer class="footer">
    <div class="footer-info">
      <div class="company">Travik Electrical Services</div>
      <div><span class="label">Ph:</span> 02 9416 3827<span class="gap"></span><span class="label">E-mail:</span> service@travik.com.au</div>
      <div><span class="label">Website:</span> www.travik.com.au</div>
      <div><span class="label">Address:</span> PO Box 4810, Marrickville NSW 2204</div>
    </div>
    <div class="brand-box">
      <span class="dot"></span><span class="name">TRAVIK</span>
    </div>
  </footer>

</main>
</body>
</html>
```